Warehouse fit out company needed website design!

Colour scheme to match attached business logo (faded lemon yellow, charcoal and white.

My business is doing warehouse fit outs using heavy duty storage systems such as pallet racking, mezzanine floors, cantilever racking and shelving.

Website to be modern style and easy for the customer to navigate through.

Please visit this competitors website for example of the type of design I would like www.brindlevault.com.au

My business will be providing the exact same service and products so this will give you a great understanding of what I am chasing from my website

Target Market(s)

Small to large businesses with warehouses to store their product.

Coding

Coded - Design and coding required

Number of Pages Required

5+ page

Colors
fbed22
ffffff
1b1b1b

Requirements
Must have
• Bold banner incorporating my attached logo on each page with drop boxes for products, services, contact us
• Home page to have "about us" write up section and images
Nice to have
• Modern style layout and easy to navigate through for the client

```html
<!DOCTYPE html>
<html lang="en">
<head>
<meta charset="utf-8">
<title>Rackwell — Warehouse Fit Outs</title>
<link rel="stylesheet" href="https://fonts.googleapis.com/css2?family=Montserrat:wght@500;600;700;800&family=Open+Sans:wght@400;600&display=swap">
<style>
:root{
  --yellow:#fbed22;
  --yellow-pale:#fdf38a;
  --charcoal:#1b1b1b;
  --ink:#333;
  --body:#555;
  --grey-band:#e0e0e0;
  --footer:#3a393d;
  --footer-text:#d4d4d8;
  --white:#fff;
}
*{margin:0;padding:0;box-sizing:border-box}
html,body{width:1200px;height:2469px;overflow:hidden;background:var(--white)}
body{position:relative;font-family:"Open Sans",sans-serif;color:var(--ink)}
.abs{position:absolute}
.brand{font-family:"Montserrat",sans-serif;font-weight:800;color:var(--charcoal);letter-spacing:2px;text-transform:uppercase}

/* Hero */
.hero-art{position:absolute;left:0;top:0;width:1200px;height:745px}
.site-header{left:235px;top:33px;width:730px;height:49px;background:var(--white);display:flex;align-items:center;padding:0 18px}
.site-header .brand{font-size:24px;width:180px}
.main-nav{display:flex;align-items:center;font-family:"Montserrat",sans-serif;font-size:9px;font-weight:700;color:var(--charcoal);margin-left:5px;height:100%}
.main-nav a{text-decoration:none;color:inherit;padding:0 6px;height:100%;display:flex;align-items:center;position:relative}
.main-nav a.active{color:#e9d800}
.main-nav a.active::after{content:"";position:absolute;left:0;right:0;bottom:0;height:3px;background:var(--yellow)}
.main-nav .sep{color:#aaa;font-weight:400;font-size:8px}
.main-nav .caret{font-size:8px;margin-left:3px}
.call{margin-left:auto;border-left:1px solid #ccc;padding-left:14px;height:28px;display:flex;flex-direction:column;justify-content:center}
.call small{font-family:"Montserrat",sans-serif;font-size:8px;font-weight:600;color:var(--charcoal);display:flex;align-items:center;gap:5px}
.call strong{font-family:"Montserrat",sans-serif;font-size:16px;font-weight:700;color:var(--charcoal);line-height:1.1}

.slider-dots{left:91px;top:258px;width:10px}
.hero-title{left:232px;top:196px;font-family:"Montserrat",sans-serif;font-weight:700;font-size:45px;line-height:52px;color:var(--white);text-transform:uppercase}
.hero-rule{left:235px;top:320px;width:62px;height:2px;background:var(--white)}
.hero-copy{left:235px;top:348px;width:350px;font-size:10.5px;line-height:15px;color:#eee}
.btn{display:flex;align-items:center;justify-content:space-between;background:var(--yellow);border-radius:22px;font-family:"Montserrat",sans-serif;font-weight:700;font-size:11.5px;color:var(--charcoal);text-transform:uppercase;padding:0 4px 0 22px}
.btn .arrow{width:32px;height:32px;border-radius:50%;background:var(--charcoal);display:flex;align-items:center;justify-content:center}
.hero-btn{left:235px;top:420px;width:187px;height:40px}
.scroll{left:540px;top:576px;width:120px;text-align:center;font-family:"Montserrat",sans-serif;font-size:9px;color:var(--white)}
.mouse{left:589px;top:602px;width:21px;height:42px;border:1.5px solid var(--white);border-radius:11px}
.mouse::after{content:"";position:absolute;left:9px;top:6px;width:1px;height:7px;background:var(--white)}

/* Products */
.product{top:793px;width:168px}
.product-frame{position:relative;width:168px;height:144px;background:var(--yellow);border-radius:0 22px 22px 0}
.product-photo{position:absolute;left:13px;top:11px;width:143px;height:121px}
.product h3{margin-top:20px;text-align:center;font-family:"Montserrat",sans-serif;font-size:11.5px;font-weight:600;color:var(--ink);text-transform:uppercase}
.product .dash{width:24px;height:1px;background:var(--ink);margin:12px auto 0}

/* About */
.about-band{left:0;top:1048px;width:1200px;height:503px;background:var(--grey-band)}
.eyebrow{left:235px;top:1111px;font-family:"Montserrat",sans-serif;font-size:11px;font-weight:600;color:var(--ink);display:flex;align-items:center;gap:12px}
.eyebrow::before{content:"";width:18px;height:1px;background:var(--ink)}
.about-title{left:235px;top:1134px;font-family:"Montserrat",sans-serif;font-size:20px;font-weight:600;color:var(--ink)}
.about-title b{font-weight:800;color:var(--charcoal)}
.about-copy{left:235px;top:1180px;width:418px;font-size:10.3px;line-height:15px;color:var(--body);text-align:justify}
.about-copy p+p{margin-top:15px}
.about-btn{left:235px;top:1446px;width:148px;height:40px}
.about-photo-a{left:692px;top:1121px;width:273px;height:327px}
.about-photo-b{left:748px;top:1320px;width:388px;height:275px;border:8px solid var(--white);background-clip:padding-box}

/* Benefits */
.benefit-block{left:464px;top:1638px;width:170px;height:146px;background:var(--yellow);border-radius:0 24px 0 0}
.benefit-kicker{left:235px;top:1724px;font-family:"Montserrat",sans-serif;font-size:18px;font-weight:500;color:var(--charcoal);text-transform:uppercase}
.benefit-brand{left:235px;top:1747px;width:208px;text-align:right;font-size:30px}
.benefit-rule{left:394px;top:1796px;width:47px;height:1px;background:var(--charcoal)}
.benefit-copy{left:235px;top:1823px;width:210px;font-size:10.3px;line-height:15px;color:var(--body);text-align:justify;text-align-last:right}
.video{left:537px;top:1720px;width:428px;height:298px;border-radius:14px;box-shadow:0 8px 18px rgba(0,0,0,.2);overflow:hidden}
.play{left:712px;top:1830px;width:76px;height:76px;border-radius:50%;background:var(--white);display:flex;align-items:center;justify-content:center}

/* Footer */
.site-footer{left:0;top:2102px;width:1200px;height:367px;background:var(--footer)}
.footer-brand{left:235px;top:2148px;font-size:30px;color:var(--white)}
.footer-about{left:235px;top:2200px;width:230px;font-size:9.5px;line-height:15px;color:var(--footer-text)}
.footer-col{top:2158px;width:140px;color:var(--footer-text)}
.footer-col h4{font-family:"Montserrat",sans-serif;font-size:11px;font-weight:700;color:var(--white);letter-spacing:.5px;margin-bottom:16px}
.footer-col li{list-style:none;font-size:9px;line-height:22.5px;color:var(--footer-text)}
.rule-light{left:235px;width:730px;height:1px;background:#55545a}
.contact{top:2335px;display:flex;align-items:center;gap:10px;color:var(--white)}
.contact small{display:block;font-size:9px;color:var(--footer-text)}
.contact strong{display:block;font-weight:600;font-size:13.5px;line-height:15px;color:var(--white)}
.contact-divider{top:2330px;width:1px;height:46px;background:#55545a}
.copyright{left:235px;top:2419px;font-size:8px;color:var(--footer-text)}
.socials{left:852px;top:2412px;display:flex;gap:6px}
.socials span{width:23px;height:23px;border-radius:50%;background:#4c8fd6}
.socials span:nth-child(2){background:#8aa6c4}
.socials span:nth-child(3){background:#8c8c90}
.socials span:nth-child(4){background:#9a9a9e}
</style>
</head>
<body>

<svg class="hero-art" viewBox="0 0 1200 745" role="img" aria-label="Warehouse interior with red pallet racking, stacked cartons and a forklift, darkened">
  <defs>
    <linearGradient id="heroShade" x1="0" y1="0" x2="0" y2="1">
      <stop offset="0" stop-color="#3f3b38"/>
      <stop offset=".5" stop-color="#6a5f56"/>
      <stop offset="1" stop-color="#7d7064"/>
    </linearGradient>
  </defs>
  <polygon points="0,0 1200,0 1200,618 982,601 591,700 324,591 0,690" fill="url(#heroShade)"/>
  <polygon points="0,690 324,591 0,742" fill="var(--yellow-pale)"/>
  <polygon points="324,591 591,700 982,601 1000,604 591,725" fill="var(--yellow)"/>
</svg>

<header class="site-header abs">
  <div class="brand">Rackwell</div>
  <nav class="main-nav">
    <a class="active">HOME</a><span class="sep">/</span>
    <a>ABOUT</a><span class="sep">/</span>
    <a>PRODUCTS<span class="caret">⌄</span></a><span class="sep">/</span>
    <a>SERVICES<span class="caret">⌄</span></a><span class="sep">/</span>
    <a>BLOG</a><span class="sep">/</span>
    <a>CONTACT<span class="caret">⌄</span></a>
  </nav>
  <div class="call">
    <small><svg width="11" height="8" viewBox="0 0 11 8"><rect width="11" height="8" fill="var(--charcoal)"/><path d="M0 0l5.5 4.5L11 0" stroke="#fff" fill="none"/></svg>CALL US TODAY</small>
    <strong>000.123.4567</strong>
  </div>
</header>

<svg class="slider-dots abs" width="10" height="140" viewBox="0 0 10 140">
  <circle cx="5" cy="4" r="4" fill="#fff"/>
  <line x1="5" y1="19" x2="5" y2="31" stroke="#fff"/>
  <circle cx="5" cy="47" r="3.5" fill="none" stroke="#fff"/>
  <line x1="5" y1="62" x2="5" y2="74" stroke="#fff"/>
  <circle cx="5" cy="90" r="3.5" fill="none" stroke="#fff"/>
  <line x1="5" y1="105" x2="5" y2="117" stroke="#fff"/>
  <circle cx="5" cy="133" r="3.5" fill="none" stroke="#fff"/>
</svg>

<h1 class="hero-title abs">Rackwell Supply<br>Pallet Racking</h1>
<div class="hero-rule abs"></div>
<p class="hero-copy abs">Lorem ipsum dolor sit amet, consectetur adipiscing elit. Fusce porttitor eu sapien ac dictum. Praesent molestie elit sit amet lacus mattis mattis.Lorem ipsum dolor sit amet, consectetur adipiscing elit.</p>
<div class="btn hero-btn abs">Get a free quote<span class="arrow"><svg width="8" height="10" viewBox="0 0 8 10"><path d="M2 1l4 4-4 4" stroke="var(--yellow)" stroke-width="1.5" fill="none"/></svg></span></div>
<div class="scroll abs">SCROLL DOWN</div>
<div class="mouse abs"></div>

<section>
  <div class="product abs" style="left:235px">
    <div class="product-frame"><div class="product-photo" role="img" aria-label="Aisle of pallet racking loaded with cartons" style="background:linear-gradient(180deg,#8a6f5c,#b89a80 60%,#6b5548)"></div></div>
    <h3>Pallet Racking</h3><div class="dash"></div>
  </div>
  <div class="product abs" style="left:422px">
    <div class="product-frame"><div class="product-photo" role="img" aria-label="Mezzanine floor in a bright warehouse" style="background:linear-gradient(180deg,#9aa3b4,#d9dde3 55%,#b9bfc8)"></div></div>
    <h3>Mezzanine Floors</h3><div class="dash"></div>
  </div>
  <div class="product abs" style="left:609px">
    <div class="product-frame"><div class="product-photo" role="img" aria-label="Blue and yellow cantilever racking arms" style="background:linear-gradient(135deg,#c3c6c8,#d8c04a 45%,#3d5a8a)"></div></div>
    <h3>Cantilever Racking</h3><div class="dash"></div>
  </div>
  <div class="product abs" style="left:796px">
    <div class="product-frame"><div class="product-photo" role="img" aria-label="Rows of steel shelving with stock" style="background:linear-gradient(180deg,#6e6468,#9a8f92 55%,#55505a)"></div></div>
    <h3>Shelving</h3><div class="dash"></div>
  </div>
</section>

<div class="about-band abs"></div>
<div class="eyebrow abs">ABOUT US</div>
<h2 class="about-title abs">WELCOME TO <b>RACKWELL</b></h2>
<div class="about-copy abs">
  <p>Lorem ipsum dolor sit amet, consectetur adipiscing elit. Fusce porttitor eu sapien ac dictum. Praesent molestie elit sit amet lacus mattis mattis. Fusce id tellus quis est dapibus porttitor. Mauris eu purus id justo dignissim tincidunt id in eros. Aenean vel leo in felis aliquam pretium. Maecenas quis hendrerit metus. Praesent a neque vitae augue congue congue. Curabitur sem diam, luctus molestie urna sit amet, porttitor consequat sem. Mauris gravida libero ut libero viverra, eu posuere odio cursus. Curabitur eu tortor sed ex fermentum semper. Sed non lobortis justo, vel molestie sapien. Phasellus eget nulla imperdiet, dapibus ligula in, dignissim felis. Nullam vel vestibulum nulla, non elementum dui. Morbi sed molestie quam.</p>
  <p>Etiam dictum, elit egestas pretium pulvinar, enim nisl laoreet massa, sit amet volutpat dui ligula et libero. Interdum et malesuada fames ac ante ipsum primis in faucibus. Donec et felis ac leo feugiat pharetra. Sed sodales, erat eu volutpat commodo, quam lacus pharetra libero, in feugiat nisl enim quis lacus. Pellentesque at laoreet augue. In bibendum enim mi, sollicitudin sollicitudin arcu efficitur a. Etiam nec orci vitae urna venenatis tristique. Nunc pellentesque volutpat ligula, nec hendrerit lectus.</p>
</div>
<div class="btn about-btn abs">Read more<span class="arrow"><svg width="8" height="10" viewBox="0 0 8 10"><path d="M2 1l4 4-4 4" stroke="var(--yellow)" stroke-width="1.5" fill="none"/></svg></span></div>
<div class="about-photo-a abs" role="img" aria-label="Steel mezzanine platform with blue safety railings" style="background:linear-gradient(180deg,#1d2230,#3b5b9a 35%,#8e9aa8 60%,#4a5468)"></div>
<div class="about-photo-b abs" role="img" aria-label="Blue cantilever racking holding orange timber lengths" style="background:linear-gradient(160deg,#c8ccd0,#b87850 45%,#9a5a38 70%,#8a8a8a)"></div>

<div class="benefit-block abs"></div>
<div class="benefit-kicker abs">See the benefits of</div>
<div class="benefit-brand brand abs">Rackwell</div>
<div class="benefit-rule abs"></div>
<p class="benefit-copy abs">Lorem ipsum dolor sit amet, consectetur adipiscing elit. Fusce porttitor eu sapien ac dictum. Praesent molestie elit sit amet lacus mattis mattis. Fusce id tellus quis est dapibus porttitor. Mauris eu purus id justo dignissim tincidunt id in eros. Aenean vel leo in felis aliquam pretium.</p>
<div class="video abs" role="img" aria-label="Video still of an orange and blue mezzanine structure in an empty warehouse" style="background:linear-gradient(180deg,#d6dbe0,#4b7cc0 30%,#d0562c 52%,#b9bcc2 80%,#dcdde0)"></div>
<div class="play abs"><svg width="30" height="32" viewBox="0 0 30 32"><path d="M4 2l24 14L4 30Z" fill="var(--yellow)"/></svg></div>

<footer class="site-footer abs"></footer>
<div class="footer-brand brand abs">Rackwell</div>
<p class="footer-about abs">Lorem ipsum dolor sit amet, consectetur adipiscing elit. Fusce porttitor eu sapien ac dictum. Praesent molestie elit sit amet lacus mattis mattis. Fusce id tellus quis est dapibus porttitor. Mauris eu purus id justo dignissim tincidunt id in eros.</p>
<div class="footer-col abs" style="left:529px"><h4>QUICK LINKS</h4><ul><li>About</li><li>Services</li><li>Products</li><li>Contact</li></ul></div>
<div class="footer-col abs" style="left:680px"><h4>OUR PRODUCTS</h4><ul><li>Pallet Racking</li><li>Mezzanine Floors</li><li>Cantilever Racking</li><li>Shelving</li></ul></div>
<div class="footer-col abs" style="left:830px"><h4>SUPPORT</h4><ul><li>Help Center</li><li>Privacy Policy</li><li>Partner Program</li></ul></div>
<div class="rule-light abs" style="top:2314px"></div>

<div class="contact abs" style="left:274px">
  <svg width="32" height="32" viewBox="0 0 32 32" fill="none" stroke="#fff" stroke-width="1.4"><path d="M8 3l5 6-3 3c2 4 5 7 9 9l3-3 6 5-3 5C15 28 4 17 3 6Z"/><path d="M19 4a10 10 0 0 1 9 9M19 9a5 5 0 0 1 4 4"/></svg>
  <div><small>Call Us Now</small><strong>(000) 123-4567</strong></div>
</div>
<div class="contact-divider abs" style="left:479px"></div>
<div class="contact abs" style="left:514px">
  <svg width="32" height="26" viewBox="0 0 32 26" fill="none" stroke="#fff" stroke-width="1.4"><rect x="1" y="2" width="30" height="22"/><path d="M1 2l15 13L31 2M1 24l11-11M31 24L20 13"/></svg>
  <div><small>Email Us Now</small><strong>info@rackwell.com</strong></div>
</div>
<div class="contact-divider abs" style="left:703px"></div>
<div class="contact abs" style="left:733px">
  <svg width="32" height="34" viewBox="0 0 32 34" fill="none" stroke="#fff" stroke-width="1.4"><path d="M16 26C9 17 7 14 7 10a9 9 0 0 1 18 0c0 4-2 7-9 16Z"/><circle cx="16" cy="10" r="3.5"/><path d="M9 22H4L1 33h30l-3-11h-5"/></svg>
  <div><small>Address</small><strong>390 Lorem ipsum St. Ste.C<br>Dolor Sit, CA 94565</strong></div>
</div>
<div class="rule-light abs" style="top:2390px"></div>
<div class="copyright abs">Rackwell © 2019. All Rights Reserved</div>
<div class="socials abs"><span></span><span></span><span></span><span></span></div>

</body>
</html>
```